Business Card Design needed for logo design project

This project is linked to a href='http://jobs.pixelfennel.example/job.aspx?id=412907'Tide Nook: Design a logo for our new trailer boat syndication business in Sydney
Our company needs a Business Card Design. Please refer to our original project in the link above.
I would like a relatively simple and classy business card design. could you please also use small symbols for identifying contact info eg. mobile, web and email?
Updates
Please see my new project to design a business card for a trailer boat syndication business in Sydney, Australia.
Industry/Entity Type
Business
Look and feel
Each slider illustrates characteristics of the customer's brand and the style your logo design should communicate.

```html
<!DOCTYPE html>
<html lang="en">
<head>
<meta charset="utf-8">
<title>Tide Nook — Business Card</title>
<link rel="stylesheet" href="https://fonts.googleapis.com/css2?family=Exo+2:wght@400;600;800&display=swap">
<style>
  :root {
    --bg: #1b1b1c;
    --card: #232425;
    --card-deep: #141515;
    --teal: #2fa9b4;
    --teal-dark: #2b5a5c;
    --grey: #8a8c8e;
    --text: #e9eaea;
    --muted: #b9bbbc;
  }
  * { box-sizing: border-box; margin: 0; padding: 0; }
  html, body { width: 1200px; height: 900px; overflow: hidden; }
  body {
    background: radial-gradient(circle at 50% 45%, #2a2a2b 0%, var(--bg) 70%);
    font-family: "Exo 2", sans-serif;
    position: relative;
  }
  .card {
    position: absolute;
    top: 290px;
    width: 540px;
    height: 320px;
    border-radius: 18px;
    overflow: hidden;
    background: var(--card);
    box-shadow: 0 18px 40px rgba(0,0,0,.6);
  }
  .card--front { left: 40px; }
  .card--back { left: 620px; }

  .front-artwork {
    position: absolute; left: 0; right: 0; top: 0; height: 200px;
    background: linear-gradient(160deg, #3a3c3e 0%, #4f5a5b 40%, #2f4748 65%, #232425 100%);
  }

  .brand {
    position: absolute;
    font-weight: 800;
    color: var(--teal);
    letter-spacing: .5px;
    line-height: 1;
  }
  .tagline {
    position: absolute;
    font-weight: 600;
    color: var(--text);
    letter-spacing: .6px;
    white-space: nowrap;
  }
  .card--front .brand { left: 36px; top: 220px; font-size: 48px; }
  .card--front .tagline { left: 38px; top: 274px; font-size: 10px; }

  /* back */
  .skyline-photo {
    position: absolute; left: 0; right: 0; top: 0; height: 150px;
    background: linear-gradient(180deg, #3a3c3d 0%, #56585a 55%, #262728 100%);
    opacity: .8;
  }
  .back-fade {
    position: absolute; inset: 0;
    background: linear-gradient(180deg, rgba(35,36,37,0) 30%, var(--card-deep) 100%);
  }
  .card--back .brand { right: 40px; top: 54px; font-size: 34px; }
  .card--back .tagline { right: 40px; top: 92px; font-size: 8.5px; }
  .holder {
    position: absolute; left: 36px; top: 150px;
    font-size: 19px; font-weight: 600; color: var(--text);
    letter-spacing: .5px;
  }
  .holder .role { font-size: 10px; color: var(--teal); font-weight: 400; margin-left: 6px; }
  .contacts {
    position: absolute; left: 36px; top: 200px;
    list-style: none;
    font-size: 11px; color: var(--muted); letter-spacing: .4px;
  }
  .contacts li { display: flex; align-items: center; gap: 8px; margin-bottom: 7px; }
  .contact-icon {
    width: 14px; height: 14px; background: var(--teal); border-radius: 2px;
    display: flex; align-items: center; justify-content: center;
  }
  .address {
    position: absolute; left: 330px; top: 150px;
    padding-left: 14px; border-left: 1px solid var(--grey);
    font-size: 10.5px; line-height: 1.7; color: var(--muted);
    font-style: normal; letter-spacing: .4px;
  }
</style>
</head>
<body>

<section class="card card--front">
  <div class="front-artwork" role="img" aria-label="Night photograph of a harbour bridge and city skyline with a decorative sweep graphic"></div>
  <div class="brand">Tide Nook</div>
  <div class="tagline">TRAILER BOAT SYNDICATION AND MANAGEMENT</div>
</section>

<section class="card card--back">
  <div class="skyline-photo" role="img" aria-label="Faded photograph of a harbour bridge and city skyline"></div>
  <div class="back-fade"></div>
  <div class="brand">Tide Nook</div>
  <div class="tagline">TRAILER BOAT SYNDICATION AND MANAGEMENT</div>

  <h1 class="holder">HARRIET LOWE<span class="role">TITLE / POSITION</span></h1>

  <ul class="contacts">
    <li>
      <span class="contact-icon"><svg width="9" height="9" viewBox="0 0 10 10"><rect x="2.5" y="0.5" width="5" height="9" rx="1" fill="none" stroke="#fff" stroke-width="1.2"/></svg></span>
      +61 20 555 014
    </li>
    <li>
      <span class="contact-icon"><svg width="10" height="8" viewBox="0 0 10 8"><rect x="0.6" y="0.6" width="8.8" height="6.8" fill="none" stroke="#fff" stroke-width="1.1"/><path d="M0.6 0.6 L5 4.5 L9.4 0.6" fill="none" stroke="#fff" stroke-width="1.1"/></svg></span>
      INFO@TIDENOOK.COM.AU
    </li>
    <li>
      <span class="contact-icon"><svg width="10" height="10" viewBox="0 0 10 10"><circle cx="5" cy="5" r="4.2" fill="none" stroke="#fff" stroke-width="1"/><ellipse cx="5" cy="5" rx="1.8" ry="4.2" fill="none" stroke="#fff" stroke-width="0.9"/><path d="M0.8 5 H9.2" stroke="#fff" stroke-width="0.9"/></svg></span>
      WWW.TIDENOOK.COM.AU
    </li>
  </ul>

  <address class="address">
    FAKE ADDRESS 61 LN.<br>
    9327 MARLOW BAY, CA 12345<br>
    HARBOURTON
  </address>
</section>

</body>
</html>
```